Wound Care Flyer

Looking for a Trifold brochure that is modern and has a high aesthetic. (Specialty services) Would like the colors to center around Black and Gold. Possibly updating the logo. Attached is the old brochure and a document about our services.

```html
<!DOCTYPE html>
<html lang="en">
<head>
<meta charset="utf-8">
<title>Cedarline Wounds – Trifold Brochure</title>
<link rel="stylesheet" href="https://fonts.googleapis.com/css2?family=Montserrat:wght@400;500;600;700&family=Cinzel:wght@600;700&display=swap">
<style>
:root{
  --black:#060606;
  --white:#f4f4f4;
  --gold:#c9a55f;
  --stage:#cbcbcb;
  --gold-grad:linear-gradient(135deg,#a9843f 0%,#c9a55f 45%,#8a6a2e 100%);
}
*{box-sizing:border-box;margin:0;padding:0}
html,body{width:706px;height:1200px;overflow:hidden}
body{background:var(--stage);font-family:"Montserrat",sans-serif;color:var(--white);position:relative}

.sheet{position:absolute;left:13px;width:680px;height:470px;display:flex;background:var(--black);box-shadow:0 6px 18px rgba(0,0,0,.35)}
.sheet--outside{top:100px}
.sheet--inside{top:630px}
.panel{position:relative;width:226.67px;height:100%;overflow:hidden;background:var(--black)}

.gold-wedge{position:absolute;inset:0;background:var(--gold-grad)}
.photo{position:absolute;border:3px solid var(--white);border-radius:30px 6px 30px 6px;overflow:hidden}
.photo--blue{background:linear-gradient(160deg,#d9dde2 0%,#8fb0cf 45%,#3f6d9a 100%)}
.photo--warm{background:linear-gradient(160deg,#c9c3bd 0%,#8e7a6c 50%,#3f5e7a 100%)}
.photo--office{background:linear-gradient(160deg,#dfe5ea 0%,#9aa8b5 50%,#4c5866 100%)}
.photo--skin{background:linear-gradient(150deg,#6c6f86 0%,#b88a66 50%,#e6e4e4 100%)}
.photo--clinic{background:linear-gradient(160deg,#e6e9ec 0%,#b7c4cf 50%,#4d7fa5 100%)}

.heading{font-weight:600;color:var(--gold);font-size:11.5px;line-height:1.15}
.body{font-size:7.8px;line-height:1.3;color:var(--white)}
.body strong{font-weight:600}

.brand{position:absolute;left:0;right:0;text-align:center}
.brand__ring{width:60px;height:60px;border:2px solid var(--gold);border-radius:50%;margin:0 auto 9px}
.brand__name{font-weight:500;color:var(--gold);font-size:12px;letter-spacing:3px;line-height:1.35;text-transform:uppercase}

.contact{position:absolute;left:18px;top:188px;width:190px;padding:10px 12px;background:var(--black);border:2px solid var(--gold);border-radius:8px}
.contact__title{font-family:"Cinzel",serif;font-weight:700;color:var(--gold);font-size:18px;letter-spacing:.5px;margin-bottom:4px}
.contact__line{display:flex;align-items:center;gap:6px;font-weight:600;font-size:12.5px;line-height:1.45}
.contact__line--mail{font-size:7px;font-weight:500;margin-top:2px}
.contact__line svg{flex:none}

.cover-title{position:absolute;left:0;right:0;bottom:26px;text-align:center;font-family:"Cinzel",serif;font-weight:700;color:var(--white);line-height:1}
.cover-title__small{font-size:12px}
.cover-title__big{font-size:20px;margin-top:3px}

.services{position:absolute;left:14px;right:14px;top:140px;bottom:14px;border:1.5px solid var(--gold);border-radius:10px;padding:9px 8px 8px 8px}
.service{display:flex;gap:7px;margin-bottom:6px}
.service__icon{flex:none;width:18px;height:18px;border:1.3px solid var(--gold);border-radius:50%;display:flex;align-items:center;justify-content:center}
.service__title{font-weight:600;font-size:8px;margin-bottom:2px}
.ticks{list-style:none}
.ticks li{display:flex;align-items:center;gap:4px;font-size:7.2px;line-height:1.5}
.ticks li::before{content:"";flex:none;width:5px;height:5px;border-radius:50%;background:var(--gold)}
.note{font-size:6.6px;font-weight:600;line-height:1.25;margin:1px 0 3px}
.service__text{font-size:7.2px;line-height:1.25}

.benefit{display:flex;gap:8px;margin-bottom:8px}
.benefit__icon{flex:none;width:22px;height:22px;border-radius:50%;background:var(--gold);display:flex;align-items:center;justify-content:center}
.benefit__title{font-weight:600;font-size:8.4px;margin-bottom:1px}
.benefit .body{font-size:7.6px;line-height:1.25}
</style>
</head>
<body>

<section class="sheet sheet--outside">
  <article class="panel panel--intro">
    <div class="gold-wedge" style="clip-path:polygon(0 100%,100% 72%,100% 100%)"></div>
    <div style="position:absolute;left:18px;right:14px;top:22px">
      <h2 class="heading">Leaders in Mobile Advanced<br>Wound Care.</h2>
      <p class="body" style="margin-top:6px">We provide an additional layer of expertise by utilizing advanced the advanced technology of biological skin substitute grafts. We pride ourselves in working in close coordination with the patient's care team, including home health services and the primary care physician (PCP).<br>We ensure seamless integration without duplicating services prioritizing collaborative care, sharing detailed notes and working closely with the patient's home health team on days between visits.</p>
      <p class="body" style="margin-top:8px">Serving the greater North Ridgeview area. (Ashford, Maple Hollow, Brookfield, Pine Crest, Elmwood, Stonebridge, Fairview, Lakeside)</p>
    </div>
    <div class="photo photo--clinic" role="img" aria-label="Doctor in white coat with stethoscope holding a tablet beside a patient" style="left:14px;top:262px;width:198px;height:190px"></div>
  </article>

  <article class="panel panel--contact">
    <div class="photo--blue" role="img" aria-label="Two smiling clinicians in scrubs looking at a laptop" style="position:absolute;left:0;top:0;width:100%;height:320px"></div>
    <div style="position:absolute;inset:0;background:var(--black);clip-path:polygon(0 320px,100% 255px,100% 100%,0 100%)"></div>
    <div class="contact">
      <div class="contact__title">CONTACT US</div>
      <div class="contact__line">
        <svg width="11" height="11" viewBox="0 0 24 24"><path fill="#c9a55f" d="M6.6 10.8a15.5 15.5 0 0 0 6.6 6.6l2.2-2.2c.3-.3.7-.4 1-.2 1.1.4 2.3.6 3.6.6.6 0 1 .4 1 1V20c0 .6-.4 1-1 1A17 17 0 0 1 3 4c0-.6.4-1 1-1h3.5c.6 0 1 .4 1 1 0 1.3.2 2.5.6 3.6.1.3 0 .7-.2 1z"/></svg>
        (555) 014-2387
      </div>
      <div class="contact__line">
        <svg width="12" height="11" viewBox="0 0 24 22"><path fill="#c9a55f" d="M6 0h12v6H6zM2 7h20a2 2 0 0 1 2 2v8h-5v5H5v-5H0V9a2 2 0 0 1 2-2zm5 8v5h10v-5z"/></svg>
        (555) 014-2390
      </div>
      <div class="contact__line contact__line--mail">
        <svg width="10" height="8" viewBox="0 0 20 14"><rect x="1" y="1" width="18" height="12" fill="none" stroke="#c9a55f" stroke-width="1.6"/><path d="M1 1l9 7 9-7" fill="none" stroke="#c9a55f" stroke-width="1.6"/></svg>
        hello@cedarlinewounds.example
      </div>
    </div>
    <div class="brand" style="top:330px">
      <div class="brand__ring"></div>
      <div class="brand__name">Cedarline<br>Wounds</div>
    </div>
  </article>

  <article class="panel panel--cover">
    <div class="gold-wedge" style="clip-path:polygon(0 58%,100% 52%,100% 100%,0 100%)"></div>
    <div class="brand" style="top:20px">
      <div class="brand__ring"></div>
      <div class="brand__name">Cedarline<br>Wounds</div>
    </div>
    <div class="photo photo--warm" role="img" aria-label="Caregiver holding the hands of a smiling senior patient" style="left:14px;top:150px;width:198px;height:200px"></div>
    <div class="cover-title">
      <div class="cover-title__small">CEDARLINE WOUNDS</div>
      <div class="cover-title__big">MOBILE<br>WOUND CARE</div>
    </div>
  </article>
</section>

<section class="sheet sheet--inside">
  <article class="panel panel--about">
    <div class="gold-wedge" style="clip-path:polygon(0 76%,0 100%,100% 100%,100% 96%)"></div>
    <p class="body" style="position:absolute;left:20px;right:12px;top:20px;font-size:8.5px;line-height:1.2">With a focus on convenience, expertise, and compassion, we bring the highest standard of wound care directly to the patient's home. Working side-by-side with the patient's physician, our team of experienced specialists utilize cutting-edge technology and personalized treatment plans to ensure optimal healing and comfort. From thorough wound assessments to advanced therapies and ongoing support, we prioritize the wellbeing of our patients everystep of the way. Whether it's managing chronic wounds, postsurgery recovery, we go above and beyond to provide comprehensive and compassionate care. With our concierge approach, we aim to make the healing journey as seamless and comfortable as possible, empowering our patients to live their best lives.</p>
    <div class="photo photo--office" role="img" aria-label="Medical team of doctors and colleagues talking in a bright hallway" style="left:16px;top:255px;width:196px;height:196px"></div>
  </article>

  <article class="panel panel--services">
    <div class="gold-wedge" style="clip-path:polygon(0 96%,0 100%,20% 100%)"></div>
    <div style="position:absolute;left:14px;right:12px;top:22px">
      <h2 class="heading">Leaders in Mobile Advanced<br>Wound Care.</h2>
      <p class="body" style="margin-top:4px">We provide a complete wound management program for our patients that includes the use of advanced treatments, the creation of care plans, and coordination of care with other clinicians.<br><strong>Our comprehensive in-home wound care services include:</strong></p>
    </div>
    <div class="services">
      <div class="service">
        <span class="service__icon"><svg width="9" height="9" viewBox="0 0 10 10"><rect x="1" y="1" width="7" height="8" fill="none" stroke="#c9a55f"/><circle cx="6" cy="6" r="1.8" fill="none" stroke="#c9a55f"/></svg></span>
        <div>
          <div class="service__title">Advanced Wound Assessment</div>
          <ul class="ticks"><li style="align-items:flex-start;line-height:1.25">Thorough evaluation of wound type, size, and stage to develop a tailored treatment plan.</li></ul>
        </div>
      </div>
      <div class="service">
        <span class="service__icon"><svg width="9" height="9" viewBox="0 0 10 10"><path d="M2 8l5-5M6 2l2 2" stroke="#c9a55f" stroke-width="1.2" fill="none"/></svg></span>
        <div>
          <div class="service__title">Cutting-Edge Treatments</div>
          <p class="note">Utilization of the latest technologies and techniques in wound care, including:</p>
          <ul class="ticks">
            <li>Compression</li>
            <li>Biologic Skin Substitutes</li>
            <li>Negative Pressure Wound Therapy</li>
            <li>Collagen and Advanced Dressings</li>
            <li>Surgical/ Trauma Wounds</li>
            <li>Venous/ Arterial Wounds</li>
            <li>Debridements</li>
          </ul>
        </div>
      </div>
      <div class="service">
        <span class="service__icon"><svg width="9" height="9" viewBox="0 0 10 10"><rect x="2" y="1" width="6" height="8" fill="none" stroke="#c9a55f"/><path d="M3.5 4h3M3.5 6h3" stroke="#c9a55f"/></svg></span>
        <div>
          <div class="service__title">Personalized Care Plans</div>
          <p class="body service__text">Customized care plans designed to meet the specific needs of each patient, ensuring optimal healing. Coordination and direction of care for other caregivers and clinicians, including home health.</p>
          <p class="body service__text" style="margin-top:6px">Patient and Caregiver Education Providing education and support to patients and their caregivers to enhance understanding and promote self-care.</p>
        </div>
      </div>
    </div>
  </article>

  <article class="panel panel--partner">
    <div style="position:absolute;left:14px;right:10px;top:20px">
      <h2 class="heading" style="margin-bottom:7px">Partner with Cedarline<br>Wounds:</h2>
      <div class="benefit">
        <span class="benefit__icon"><svg width="11" height="11" viewBox="0 0 12 12"><path d="M6 10.5L1.5 6A2.5 2.5 0 0 1 6 2.8 2.5 2.5 0 0 1 10.5 6z" fill="#060606"/></svg></span>
        <div><div class="benefit__title">Enhanced Patient Outcomes</div><p class="body">Our specialized expertise in advanced wound care leads to faster healing times and improved patient satisfaction.</p></div>
      </div>
      <div class="benefit">
        <span class="benefit__icon"><svg width="11" height="11" viewBox="0 0 12 12"><path d="M1 1l3 3M11 1L8 4M1 11l3-3M11 11L8 8" stroke="#060606" stroke-width="1.6"/></svg></span>
        <div><div class="benefit__title">Extended Reach</div><p class="body">Our in-home services allow your patients to receive high-quality care without the need for frequent visits, reducing the burden on your resources.</p></div>
      </div>
      <div class="benefit">
        <span class="benefit__icon"><svg width="11" height="11" viewBox="0 0 12 12"><path d="M2.5 6.2l2.3 2.3 4.7-5" stroke="#060606" stroke-width="1.8" fill="none"/></svg></span>
        <div><div class="benefit__title">Professional Integrity</div><p class="body">As a trusted partner, we uphold the highest standards of care and professionalism, reflecting positively on your clinic's reputation.</p></div>
      </div>
      <div class="benefit">
        <span class="benefit__icon"><svg width="11" height="11" viewBox="0 0 12 12"><circle cx="6" cy="6" r="3.5" fill="none" stroke="#060606" stroke-width="1.6"/><circle cx="6" cy="6" r="1" fill="#060606"/></svg></span>
        <div><div class="benefit__title">Enhanced Patient Outcomes</div><p class="body">We maintain open communication with referring clinics, ensuring a coordinated approach to patient care.</p></div>
      </div>
    </div>
    <div class="photo photo--skin" role="img" aria-label="Gloved hand examining a wound on a patient's lower leg" style="left:14px;top:296px;width:200px;height:158px"></div>
  </article>
</section>

</body>
</html>
```